Hip surgeon needs a stationery design

I need a new stationery design for my private practice.
My practice is focused in hip arthroplasty (hip prosthesis).
I'd like to see designs most in blue or shades of blue.
I've uploaded my new logo to help with the task.
Also, I'm a member of some societies and I've uploaded their logos either, so I'd like to see them in some of the stationeries.
Itens list:
business card
letterhead A4
envelope
prescription block A5
one fold for A4 (please see the archive "pocket")
Personal data:
Dr. Renato L. Ferraz
CRM/PR 73915
site: www.clinicaarticular.com.br
email: dr.renato@clinicaarticular.com.br
Adress:
Rua Benedito Almeida Prates, 912
Campo Alegre - Curitiba/PR
41 35718206 I 35718207
Updates
I forgot to mention that my practice is focused primarily in hip arthroplasty (total hip prosthesis) and the target audience range from young adults to the elderly.
I also perform hip preserving surgeries (open and arthroscopic procedures) and pelvic and hip fracture surgery (trauma).
- Any "cleaner" fonts are welcome

```html
<!DOCTYPE html>
<html lang="pt-BR">
<head>
<meta charset="utf-8">
<title>Receituário – Dr. Renato L. Ferraz</title>
<link rel="stylesheet" href="https://fonts.googleapis.com/css2?family=Roboto+Condensed:wght@400;500&family=Source+Sans+3:wght@400;600&display=swap">
<style>
  :root {
    --backdrop: #b0d4ee;
    --paper: #f1f1f3;
    --brand-blue: #1a5fa8;
    --band-blue: #0b5aa6;
    --field-grey: #8a8d93;
    --contact-grey: #5d6068;
    --watermark: #d3d6e2;
  }
  * { margin: 0; padding: 0; box-sizing: border-box; }
  html, body {
    width: 1200px; height: 1000px; overflow: hidden;
    background: var(--backdrop);
  }
  .sheet {
    position: absolute; left: 280px; top: 48px;
    width: 640px; height: 904px;
    background: var(--paper);
    font-family: "Source Sans 3", sans-serif;
  }
  .brand {
    position: absolute; left: 44px; top: 44px;
    display: flex; align-items: center; gap: 8px;
  }
  .brand-dot {
    width: 42px; height: 42px; border-radius: 50%;
    background: var(--brand-blue);
  }
  .brand-text {
    font-family: "Roboto Condensed", sans-serif;
    font-weight: 500; color: var(--brand-blue); line-height: 1.05;
  }
  .brand-name { font-size: 21px; }
  .brand-specialty { font-size: 17px; }
  .contact {
    position: absolute; left: 431px; top: 36px;
    list-style: none; font-size: 8.5px; color: var(--contact-grey);
    line-height: 12px;
  }
  .contact li { display: flex; gap: 5px; }
  .contact svg { flex: none; margin-top: 2px; }
  .fields {
    position: absolute; left: 44px; top: 152px; width: 554px;
    font-size: 13px; color: var(--field-grey); letter-spacing: 0.5px;
  }
  .field-row { display: flex; gap: 40px; margin-bottom: 20px; }
  .field { display: flex; align-items: baseline; flex: 1; }
  .field-date { flex: 0 0 170px; }
  .field-line {
    flex: 1; margin-left: 4px;
    border-bottom: 2px dotted var(--field-grey); height: 10px;
  }
  .watermark {
    position: absolute; left: 155px; top: 365px;
    width: 332px; height: 332px; border-radius: 50%;
    background: var(--watermark);
  }
  .footer-band {
    position: absolute; left: 0; bottom: 0;
    width: 100%; height: 25px; background: var(--band-blue);
  }
</style>
</head>
<body>
  <main class="sheet">
    <header class="brand">
      <span class="brand-dot"></span>
      <div class="brand-text">
        <div class="brand-name">Dr. Renato L. Ferraz</div>
        <div class="brand-specialty">Cirurgia do Quadril</div>
      </div>
    </header>

    <ul class="contact">
      <li><svg width="8" height="8" viewBox="0 0 8 8"><circle cx="4" cy="4" r="4" fill="#1a5fa8"/><circle cx="4" cy="3.5" r="1.3" fill="#fff"/></svg>
        <span>Rua Benedito Almeida Prates, 912<br>Campo Alegre - Curitiba/PR</span></li>
      <li><svg width="8" height="8" viewBox="0 0 8 8"><circle cx="4" cy="4" r="4" fill="#1a5fa8"/><path d="M2.6 2.2l1 1-.5.6a3 3 0 0 0 1.2 1.2l.6-.5 1 1-.6.6C3.8 6 2 4.2 2 2.8z" fill="#fff"/></svg>
        <span>41 35718206 I 35718207</span></li>
      <li><svg width="8" height="8" viewBox="0 0 8 8"><circle cx="4" cy="4" r="4" fill="#1a5fa8"/><circle cx="4" cy="4" r="2" fill="none" stroke="#fff" stroke-width=".7"/></svg>
        <span>www.clinicaarticular.com.br</span></li>
      <li><svg width="8" height="8" viewBox="0 0 8 8"><circle cx="4" cy="4" r="4" fill="#1a5fa8"/><rect x="2" y="2.7" width="4" height="2.8" fill="none" stroke="#fff" stroke-width=".6"/></svg>
        <span>dr.renato@clinicaarticular.com.br</span></li>
    </ul>

    <section class="fields">
      <div class="field-row">
        <div class="field"><span>NOME</span><span class="field-line"></span></div>
        <div class="field field-date"><span>DATA</span><span class="field-line"></span></div>
      </div>
      <div class="field-row">
        <div class="field"><span>ENDEREÇO</span><span class="field-line"></span></div>
      </div>
    </section>

    <div class="watermark" aria-hidden="true"></div>
    <div class="footer-band"></div>
  </main>
</body>
</html>
```